Beacon Advisory Website

I currently have a website www.beaconadvisoryinc.example. We are a IT Consulting Company. Our website will pretty much tell out our services. I am looking to enhance my website and make it look more professional. Looking for very classy and Contemporary look and design for my website.

Industry/Entity Type

It Company

```html
<!DOCTYPE html>
<html lang="en">
<head>
<meta charset="utf-8">
<title>Beacon Advisory</title>
<link href="https://fonts.googleapis.com/css2?family=Bebas+Neue&family=Open+Sans:wght@400;600;700&family=Roboto+Condensed:wght@400;700&display=swap" rel="stylesheet">
<style>
:root{
  --blue:#0b86c8;
  --blue-dark:#0d3d8a;
  --ink:#333333;
  --muted:#6f6f6f;
  --gray-band:#e4e4e4;
  --footer:#2b2b2b;
  --footer-line:#3c3c3c;
  --white:#ffffff;
}
*{box-sizing:border-box;margin:0;padding:0}
html,body{width:1200px;height:2476px;overflow:hidden;background:var(--white)}
body{position:relative;font-family:"Open Sans",sans-serif;color:var(--ink)}
.abs{position:absolute}
.cond{font-family:"Roboto Condensed",sans-serif}

/* header */
.site-header{position:absolute;left:0;top:0;width:1200px;height:112px;background:var(--white)}
.brand{position:absolute;left:79px;top:30px;display:flex;align-items:center;gap:12px}
.brand-mark{width:48px;height:48px;border-radius:50%;background:var(--blue-dark)}
.brand-name{font-family:"Roboto Condensed",sans-serif;font-weight:700;font-size:30px;color:var(--blue-dark)}
.main-nav{position:absolute;left:409px;top:41px;display:flex;height:50px}
.main-nav a{font-family:"Roboto Condensed",sans-serif;font-size:19px;color:#444;text-decoration:none;line-height:50px;padding:0 17px;text-transform:uppercase}
.main-nav a.active{background:var(--blue-dark);color:var(--white);padding:0 21px}

/* hero */
.hero{position:absolute;left:0;top:112px;width:1200px;height:519px;overflow:hidden;
  background:linear-gradient(135deg,#d9dde2 0%,#f4f5f6 40%,#e6e9ec 65%,#3b3f47 100%)}
.hero-title{position:absolute;left:214px;top:205px;white-space:nowrap;font-family:"Bebas Neue",sans-serif;font-size:68px;letter-spacing:-0.5px;color:var(--blue-dark)}

/* call band */
.call-band{position:absolute;left:0;top:631px;width:1200px;height:124px;background:var(--blue);display:flex;align-items:center;justify-content:center;gap:18px;color:var(--white);font-family:"Roboto Condensed",sans-serif;font-size:31px}
.call-band strong{font-weight:700}
.call-icon{width:62px;height:62px;border:2px solid var(--white);border-radius:50%;display:flex;align-items:center;justify-content:center}

/* welcome */
.section-title{position:absolute;left:0;width:1200px;text-align:center;font-family:"Roboto Condensed",sans-serif;font-size:41px;color:#555;text-transform:uppercase}
.section-title span{color:var(--blue)}
.welcome-text{position:absolute;left:195px;top:861px;width:810px;text-align:center;font-size:15.5px;line-height:25px;color:var(--muted)}
.btn{position:absolute;width:165px;height:50px;background:var(--blue);color:var(--white);font-family:"Roboto Condensed",sans-serif;font-size:21px;text-transform:uppercase;display:flex;align-items:center;justify-content:center}

.feature{position:absolute;top:1064px;width:320px;text-align:center}
.feature-icon{width:124px;height:124px;margin:0 auto;border:2px solid var(--blue);border-radius:50%;display:flex;align-items:center;justify-content:center}
.feature h3{font-family:"Roboto Condensed",sans-serif;font-weight:400;font-size:27px;color:#333;margin-top:10px;letter-spacing:.5px}
.feature p{font-size:15px;line-height:25px;color:var(--muted);margin-top:6px;padding:0 30px}

/* services */
.services{position:absolute;left:0;top:1362px;width:1200px;height:520px;background:var(--gray-band)}
.service-card{position:absolute;top:117px;width:234px;text-align:center}
.service-photo{width:234px;height:135px;border:1px solid #cfcfcf}
.service-card h3{font-family:"Roboto Condensed",sans-serif;font-weight:400;font-size:23px;color:var(--blue);margin-top:10px;white-space:nowrap}
.service-card p{font-size:15px;line-height:25px;color:var(--muted);margin-top:8px;padding:0 8px}

/* highlights */
.highlight{position:absolute;top:1935px;display:flex;gap:14px}
.highlight-photo{width:206px;height:134px;flex:none}
.highlight h3{font-family:"Roboto Condensed",sans-serif;font-weight:400;font-size:30px;color:#444;line-height:1}
.highlight h3 span{color:var(--blue)}
.highlight p{font-size:15px;line-height:25px;color:var(--muted);margin-top:14px;width:250px}

/* footer */
.site-footer{position:absolute;left:0;top:2121px;width:1200px;height:355px;background:var(--footer);color:var(--white)}
.footer-col{position:absolute;top:26px}
.footer-col h4{font-family:"Roboto Condensed",sans-serif;font-weight:400;font-size:22px;color:var(--blue)}
.link-list{list-style:none;margin-top:14px}
.link-list li{font-size:15px;line-height:31.4px;display:flex;align-items:center;gap:9px}
.link-list li.current{color:var(--blue)}
.newsletter p{font-size:14px;line-height:25px;margin-top:14px;width:230px}
.field{width:234px;height:37px;background:#3d3d3d;font-size:14px;line-height:37px;padding-left:10px;margin-top:12px}
.field + .field{margin-top:12px}
.subscribe{width:146px;height:40px;background:var(--blue);font-family:"Roboto Condensed",sans-serif;font-size:21px;display:flex;align-items:center;justify-content:center;margin-top:21px}
.contact-row{display:flex;gap:16px;font-size:14px;line-height:21px;margin-top:14px}
.contact-row svg{flex:none;margin-top:3px}
.social-row{display:flex;align-items:center;gap:12px;font-size:15px;margin-top:14px}
.social-dot{width:47px;height:47px;border-radius:50%;background:var(--white)}
.social-row.blue .social-dot{background:var(--blue)}
.footer-rule{position:absolute;left:78px;top:292px;width:1044px;height:1px;background:var(--footer-line)}
.copyright{position:absolute;left:0;top:310px;width:1200px;text-align:center;font-size:15px}
.copyright span{color:var(--blue);font-weight:600}
</style>
</head>
<body>

<header class="site-header">
  <div class="brand"><div class="brand-mark"></div><div class="brand-name">BEACON ADVISORY</div></div>
  <nav class="main-nav">
    <a class="active">Home</a><a>About</a><a>Services</a><a>Solution</a><a>Resources</a><a>Career</a><a>Contact</a>
  </nav>
</header>

<section class="hero" role="img" aria-label="Photo of business people signing papers at a desk with a keyboard and glasses">
  <h1 class="hero-title">DELIVERING EXCEPTIONAL CLIENT SERVICE</h1>
</section>

<div class="call-band">
  <span>LOREM IPSUM IS DUMMY TEXT <strong>CALL US ON</strong></span>
  <span class="call-icon">
    <svg width="30" height="30" viewBox="0 0 24 24"><path fill="#fff" d="M6.6 10.8a15.1 15.1 0 0 0 6.6 6.6l2.2-2.2c.3-.3.7-.4 1-.2 1.1.4 2.3.6 3.6.6.6 0 1 .4 1 1V20c0 .6-.4 1-1 1A17 17 0 0 1 3 4c0-.6.4-1 1-1h3.5c.6 0 1 .4 1 1 0 1.3.2 2.5.6 3.6.1.3 0 .7-.2 1z"/></svg>
  </span>
  <strong>+1 (555) 014 2290</strong>
</div>

<h2 class="section-title" style="top:796px">Welcome to <span>Beacon Advisory</span></h2>
<p class="welcome-text">Today’s IT market is a dynamic, fast-paced industry, with ever-increasing demands. Meeting these demands for over 25 years, Beacon Advisory maintains a global presence, aggressively recruiting expertly qualified IT and Management Professionals from around the world.</p>
<div class="btn" style="left:517px;top:962px">Read More</div>

<div class="feature" style="left:73px">
  <div class="feature-icon">
    <svg width="56" height="56" viewBox="0 0 56 56" fill="#0b86c8"><circle cx="21" cy="12" r="5"/><circle cx="35" cy="12" r="5"/><rect x="15" y="19" width="12" height="12" rx="2"/><rect x="29" y="19" width="12" height="12" rx="2"/><rect x="12" y="31" width="32" height="4"/><rect x="4" y="16" width="4" height="28"/><rect x="48" y="16" width="4" height="28"/><rect x="4" y="34" width="10" height="4"/><rect x="42" y="34" width="10" height="4"/><rect x="26" y="35" width="4" height="12"/></svg>
  </div>
  <h3>Dashboards</h3>
  <p>Dashboards are a key component of every organization's Performance Management and Business...</p>
</div>
<div class="feature" style="left:444px">
  <div class="feature-icon">
    <svg width="60" height="60" viewBox="0 0 60 60" fill="#0b86c8"><ellipse cx="26" cy="12" rx="18" ry="6"/><path d="M8 16c0 4 8 7 18 7s18-3 18-7v8c0 4-8 7-18 7S8 28 8 24z"/><path d="M8 28c0 4 8 7 18 7 3 0 6-.3 8-1v8c-2 .6-5 1-8 1-10 0-18-3-18-7z"/><circle cx="45" cy="42" r="9"/><circle cx="45" cy="42" r="3.5" fill="#fff"/></svg>
  </div>
  <h3>Data Warehousing</h3>
  <p>A data warehouse is the concept of data extracted from operational systems and made available...</p>
</div>
<div class="feature" style="left:807px">
  <div class="feature-icon">
    <svg width="56" height="56" viewBox="0 0 56 56" fill="#0b86c8"><rect x="21" y="6" width="14" height="12" rx="1"/><rect x="26" y="18" width="4" height="8"/><rect x="8" y="25" width="40" height="4"/><rect x="8" y="25" width="4" height="12"/><rect x="26" y="25" width="4" height="12"/><rect x="44" y="25" width="4" height="12"/><rect x="3" y="36" width="14" height="12" rx="1"/><rect x="21" y="36" width="14" height="12" rx="1"/><rect x="39" y="36" width="14" height="12" rx="1"/></svg>
  </div>
  <h3>B P M</h3>
  <p>Beacon Advisory having Flowcraft Certified Consultants in to provide Business Process Management...</p>
</div>

<section class="services">
  <h2 class="section-title" style="top:48px">Our <span>Services</span></h2>
  <div class="service-card" style="left:76px">
    <div class="service-photo" role="img" aria-label="Photo of a trainer presenting at a whiteboard to a seated group" style="background:linear-gradient(135deg,#e8ecef,#c9d2d9)"></div>
    <h3>Technology</h3>
    <p>Beacon Advisory Training programs are perfect for individuals to enhance their...</p>
  </div>
  <div class="service-card" style="left:347px">
    <div class="service-photo" role="img" aria-label="Photo of a tablet held in hands with glowing digital app icons" style="background:linear-gradient(135deg,#1d2a3a,#4f7aa0)"></div>
    <h3>Application Developement</h3>
    <p>Drawing on our experience in all major industries, we develop solutions that meet...</p>
  </div>
  <div class="service-card" style="left:618px">
    <div class="service-photo" role="img" aria-label="Photo of two businessmen reviewing documents at a desk" style="background:linear-gradient(135deg,#c8ccd0,#4a5560)"></div>
    <h3>Enterprise Integration</h3>
    <p>As organizations work to achieve and sustain competitive advantage...</p>
  </div>
  <div class="service-card" style="left:889px">
    <div class="service-photo" role="img" aria-label="Photo of business colleagues shaking hands in an office" style="background:linear-gradient(135deg,#d8dde2,#5d6670)"></div>
    <h3>IT Consulting</h3>
    <p>Beacon Advisory Training programs are perfect for individuals to enhance their...</p>
  </div>
  <div class="btn" style="left:517px;top:404px">View All</div>
</section>

<div class="highlight" style="left:79px">
  <div class="highlight-photo" role="img" aria-label="Photo of a team working together at a laptop" style="background:linear-gradient(135deg,#dfe8f0,#a9c2d8)"></div>
  <div><h3>Our <span>Processs</span></h3><p>We bring together seasoned IT executives and battle-tested computer support personnel...</p></div>
</div>
<div class="highlight" style="left:637px">
  <div class="highlight-photo" role="img" aria-label="Overhead photo of a team meeting around a table" style="background:linear-gradient(135deg,#cdd3d8,#7d8a94)"></div>
  <div><h3>Staff <span>Augmentation</span></h3><p>For years Beacon Advisory has been offering our customers the ability to augment their existing...</p></div>
</div>

<footer class="site-footer">
  <div class="footer-col" style="left:78px">
    <h4>Useful Links</h4>
    <ul class="link-list">
      <li class="current"><svg width="14" height="8" viewBox="0 0 14 8"><path d="M0 4h12M9 1l3 3-3 3" stroke="#0b86c8" stroke-width="1.5" fill="none"/></svg>Home</li>
      <li><svg width="14" height="8" viewBox="0 0 14 8"><path d="M0 4h12M9 1l3 3-3 3" stroke="#fff" stroke-width="1.5" fill="none"/></svg>About</li>
      <li><svg width="14" height="8" viewBox="0 0 14 8"><path d="M0 4h12M9 1l3 3-3 3" stroke="#fff" stroke-width="1.5" fill="none"/></svg>Services</li>
      <li><svg width="14" height="8" viewBox="0 0 14 8"><path d="M0 4h12M9 1l3 3-3 3" stroke="#fff" stroke-width="1.5" fill="none"/></svg>Solution</li>
      <li><svg width="14" height="8" viewBox="0 0 14 8"><path d="M0 4h12M9 1l3 3-3 3" stroke="#fff" stroke-width="1.5" fill="none"/></svg>Resources</li>
      <li><svg width="14" height="8" viewBox="0 0 14 8"><path d="M0 4h12M9 1l3 3-3 3" stroke="#fff" stroke-width="1.5" fill="none"/></svg>Career</li>
      <li><svg width="14" height="8" viewBox="0 0 14 8"><path d="M0 4h12M9 1l3 3-3 3" stroke="#fff" stroke-width="1.5" fill="none"/></svg>Contact</li>
    </ul>
  </div>
  <div class="footer-col newsletter" style="left:348px">
    <h4>Newsletter</h4>
    <p>Lorem Ipsum is simply dummy text of the print and type.</p>
    <div class="field">Enter Name</div>
    <div class="field">Enter Email</div>
    <div class="subscribe">SUBSCRIBE</div>
  </div>
  <div class="footer-col" style="left:619px">
    <h4>Get In Touch</h4>
    <div class="contact-row" style="margin-top:18px"><svg width="14" height="18" viewBox="0 0 14 18"><path fill="#0b86c8" d="M7 0a7 7 0 0 0-7 7c0 5 7 11 7 11s7-6 7-11a7 7 0 0 0-7-7zm0 10a3 3 0 1 1 0-6 3 3 0 0 1 0 6z"/></svg><span>480 Harbor Lane, Suite 12<br>Millbrook, NJ 07999</span></div>
    <div class="contact-row" style="margin-top:16px"><svg width="18" height="18" viewBox="0 0 24 24"><path fill="#0b86c8" d="M6.6 10.8a15.1 15.1 0 0 0 6.6 6.6l2.2-2.2c.3-.3.7-.4 1-.2 1.1.4 2.3.6 3.6.6.6 0 1 .4 1 1V20c0 .6-.4 1-1 1A17 17 0 0 1 3 4c0-.6.4-1 1-1h3.5c.6 0 1 .4 1 1 0 1.3.2 2.5.6 3.6.1.3 0 .7-.2 1z"/></svg><span>+1 (555) 014 2290</span></div>
    <div class="contact-row" style="margin-top:18px"><svg width="18" height="14" viewBox="0 0 18 14"><rect x="1" y="1" width="16" height="12" rx="1" fill="none" stroke="#0b86c8" stroke-width="1.5"/><path d="M1 2l8 6 8-6" fill="none" stroke="#0b86c8" stroke-width="1.5"/></svg><span>Info@beaconadvisory.example</span></div>
  </div>
  <div class="footer-col" style="left:891px">
    <h4>Follow Us</h4>
    <div class="social-row"><span class="social-dot"></span>Friendly</div>
    <div class="social-row blue"><span class="social-dot"></span>Chirper</div>
    <div class="social-row blue"><span class="social-dot"></span>ProNet</div>
  </div>
  <div class="footer-rule"></div>
  <p class="copyright">© <span>Beacon Advisory Inc</span> - 2016. All Rights Reserved.</p>
</footer>

</body>
</html>
```